High-end b2b furniture company needs informational/photo brochure

Please note CHANGE IN SIZE: 11 x 25.5 overall size, tri-fold brochure. Use lots of photos and must have a high-end, clean look because we are in the interior design industry. Designer must review our website to get an idea of branding! (www.halvorquist.example).

Instructions on where all photos/images should be placed are written as the file name for the jpgs/pdfs. Please ask if file name placement instructions are not clear!

There are extra images attached to use if needed, but you do not need to use all of these. There are also several images marked for the cover, but again, no need to use all of these if it looks too crowded. This will depend upon your design. (We would prefer a relatively clean, uncrowded look.)

Thank you for your hard work. I just increased the budget for first place on this project due to the large size of this brief.

Target Market(s)

Interior designers, architects, commercial property managers, shopping mall/retail managers. We sell commercial furniture ONLY (we do not sell to end consumers and we typically do not sell furniture for the home).

Industry/Entity Type

It Company

Font styles to use
Serif
Sans Serif
Other font styles liked:
• Prefer mostly sans serif, but can use serif if design calls for it. We use variations of Gil Sans MT in much of our marketing. Can use a decorative or script font for accent, but nothing that looks "old fashioned" and no cursive or anything that looks "curly."

Colors
cadf82
add136
faa54b
f78f20
ffffff

Requirements
Must have
• An upscale feel that appeals to high-end interior designers. Photography needs to be fairly large to highlight the furniture. (Text can be placed around furniture)
Nice to have
• Ample white and dark (black or charcoal gray) space
Should not have
• No old fashioned/cursive fonts. No shadows behind photos or shadows behind text boxes. Since furniture design is our business, do not cut off the lines of our furniture designs by overlapping text or images.

```html
<!DOCTYPE html>
<html lang="en">
<head>
<meta charset="utf-8">
<title>Halvorquist Furniture – Company &amp; Furniture Spread</title>
<link href="https://fonts.googleapis.com/css2?family=Lato:wght@400;700&display=swap" rel="stylesheet">
<style>
  :root {
    --green: #add136;
    --green-label: #b5cf3a;
    --green-soft: #cadf82;
    --orange: #faa54b;
    --orange-deep: #f78f20;
    --ink: #3a3a3a;
    --paper: #ffffff;
    --backdrop: #e6e6e6;
  }
  * { box-sizing: border-box; margin: 0; padding: 0; }
  html, body { width: 1200px; height: 900px; overflow: hidden; }
  body {
    background: var(--backdrop);
    font-family: "Gill Sans", "Gill Sans MT", "Lato", sans-serif;
    color: var(--ink);
    position: relative;
  }
  .page {
    position: absolute;
    top: 25px;
    width: 547px;
    height: 847px;
    background: var(--paper);
  }
  .page--company { left: 50px; }
  .page--furniture { left: 600px; }
  .page > * { position: absolute; }

  .section-title {
    font-size: 16.5px;
    font-weight: 700;
    color: var(--green);
    top: 69px;
    letter-spacing: 0.2px;
  }
  .section-rule { top: 98px; width: 33px; height: 3px; background: var(--green); }

  .text-block {
    width: 152px;
    font-size: 10.2px;
    line-height: 13.85px;
    text-align: justify;
    hyphens: auto;
    color: #4a4a4a;
  }
  .green-bar { background: var(--green); }

  .photo { display: block; }

  .thin-rule { top: 428px; height: 4px; background: var(--green); }
  .product-shot { top: 440px; height: 155px; }
  .product-label {
    height: 29px;
    background: var(--green-label);
    color: #fff;
    font-size: 11.5px;
    font-weight: 700;
    letter-spacing: 0.6px;
    text-align: center;
    line-height: 29px;
    text-transform: uppercase;
  }
  .product-note {
    width: 155px;
    font-size: 9.2px;
    line-height: 13px;
    color: #4a4a4a;
  }
</style>
</head>
<body>

<section class="page page--company">
  <h2 class="section-title" style="left:26px;">Our Company</h2>
  <div class="section-rule" style="left:26px;"></div>

  <p class="text-block" style="left:26px; top:130px;">The central obstacle in any design project is most often communication and that’s where we shine. Halvorquist Furniture is managed by husband and wife team, Henrik and Maren Halvorquist. Their ability to complete world-class projects within various budget parameters is the result of a client-centered approach that often requires custom adjustments and creative problem-solving. Since starting our company in 2001, our team has been dedicated to providing the right furniture solutions to the most complicated design challenges.</p>

  <p class="text-block" style="left:26px; top:383px;">We proudly manufacture all of our products in the USA and maintain a strong commitment to environmentally-friendly practices. Our standard construction methods create the strongest hardwood frames in the industry using rapidly-renewable wood, sourced from the Pacific Northwest, and recycled steel springs. (Please read our environmental statement for more information.) We maintain an office and design studio in beautiful Cedar Hollow, Washington, where Henrik and Maren reside. Our standard pro-</p>

  <p class="text-block" style="left:195px; top:130px;">ducts are manufactured at our factory in Greater Los Angeles (Elm Vista, California) where we have an additional design studio. Henrik Halvorquist personally directs design and manufacturing efforts, and we work with an extensive team of gifted upholsters, craftsman, designers and CAD artists. We have the ability to complete very large runs of furniture, as well as very small orders.</p>

  <p class="text-block" style="left:195px; top:313px;">Halvorquist Furniture offers a full catalog of standard designs, as well</p>

  <p class="text-block" style="left:363px; top:130px;">as countless custom options including alternate sizes, finish options, sleeper sofas, moisture barriers, fire ratings, nailheads, contrasting welts and various firmness options in terms of foam and fill.</p>

  <p class="text-block" style="left:363px; top:227px;">We are honored to work with some of the most creative design professionals in the industry. View our recent installations or our gallery page to see more. Have a question or need a custom quote? Just give us a ring. We look forward to working with you.</p>

  <div class="photo" role="img" aria-label="The two owners standing together in a bright showroom gallery"
       style="left:195px; top:377px; width:318px; height:211px; background:linear-gradient(180deg,#9a9a9a 0%,#6e6a66 55%,#4a3f38 100%);"></div>
  <div class="green-bar" style="left:195px; top:588px; width:318px; height:10px;"></div>

  <div class="photo" role="img" aria-label="Upholsterer working with navy fabric in the workshop"
       style="left:57px; top:629px; width:143px; height:163px; background:linear-gradient(180deg,#b9ad9a 0%,#8a8580 45%,#2c3a5c 100%);"></div>
  <div class="photo" role="img" aria-label="Craftsman cutting patterns on a workshop table"
       style="left:206px; top:629px; width:143px; height:163px; background:linear-gradient(180deg,#6d5a4a 0%,#9c8c7a 50%,#d9d4cc 100%);"></div>
  <div class="photo" role="img" aria-label="CAD artist working at a computer on the factory floor"
       style="left:354px; top:629px; width:143px; height:163px; background:linear-gradient(180deg,#c9c3b8 0%,#8e8a86 50%,#4a4644 100%);"></div>
  <div class="green-bar" style="left:57px; top:792px; width:440px; height:11px;"></div>
</section>

<section class="page page--furniture">
  <h2 class="section-title" style="left:27px;">Furniture</h2>
  <div class="section-rule" style="left:27px;"></div>

  <div class="photo" role="img" aria-label="White leather swivel tub chair on a dark studio floor"
       style="left:31px; top:134px; width:487px; height:253px; background:radial-gradient(ellipse at 50% 45%,#5a5651 0%,#2a2725 55%,#141212 100%);"></div>
  <div class="green-bar" style="left:31px; top:387px; width:487px; height:13px;"></div>

  <div class="thin-rule" style="left:31px; width:155px;"></div>
  <div class="thin-rule" style="left:195px; width:153px;"></div>
  <div class="thin-rule" style="left:362px; width:155px;"></div>

  <div class="product-shot" role="img" aria-label="Yellow-orange lounge chair with dark wood arms"
       style="left:31px; width:155px; background:radial-gradient(ellipse at 50% 50%,#f6b42a 0%,#fbe2b0 45%,#ffffff 72%);"></div>
  <div class="product-shot" role="img" aria-label="Orange tufted wingback chair"
       style="left:195px; width:153px; background:radial-gradient(ellipse at 50% 50%,#f07a2a 0%,#f9cdaa 42%,#ffffff 70%);"></div>
  <div class="product-shot" role="img" aria-label="Brown striped club chair on wooden legs"
       style="left:362px; width:155px; background:radial-gradient(ellipse at 50% 50%,#6b3e30 0%,#c9aea4 45%,#ffffff 72%);"></div>

  <div class="product-label" style="left:31px; top:603px; width:155px;">Aurelle</div>
  <div class="product-label" style="left:195px; top:603px; width:153px;">Brenna</div>
  <div class="product-label" style="left:362px; top:603px; width:155px;">Belmont</div>

  <div class="photo" role="img" aria-label="Peach upholstered three-seat sofa with dark legs"
       style="left:53px; top:660px; width:204px; height:124px; background:radial-gradient(ellipse at 50% 55%,#e7a584 0%,#f6dccf 50%,#fdf3f3 80%);"></div>
  <div class="green-bar" style="left:279px; top:660px; width:10px; height:124px;"></div>

  <div class="product-label" style="left:362px; top:660px; width:153px;">Bramwell</div>
  <p class="product-note" style="left:362px; top:715px;">Available as a sofa, loveseat and lounge chair. Classic, robust arms, square back pillows and seat cushions, along with tailored welting make the Bramwell a crowd-pleaser.</p>
</section>

</body>
</html>
```